Real Estate For Sale Sign

I need to design a for sale sign. It needs to include The following information
Logo: Attached
Name: Corinne Vasquel,
Company Name: Gilded Harbor Real Estate,
Phone Number: 503-841-2096
BRE Licence Number 04817359 (Can Be small)
Sign size 24x30

I am not sure about including my website but I would like to see options with it. www.gildedharbor-example.com
Updates

Target Market(s)

Potential Buyers or Sellers of Real Estate. Must be easy to read.

Industry/Entity Type

Real Estate

Requirements
Must have
• I want it to feel luxurious and sharp.

```html
<!DOCTYPE html>
<html lang="en">
<head>
<meta charset="utf-8">
<title>Gilded Harbor Real Estate – For Sale Sign</title>
<link rel="stylesheet" href="https://fonts.googleapis.com/css2?family=Inter:wght@300;400&display=swap">
<style>
  :root {
    --backdrop: #ada290;
    --sign-navy: #00285a;
    --ink-white: #ffffff;
    --agent-blue: #17a3e6;
    --brand-mist: #a9bdd6;
    --ring-blue: #5cc4f0;
    --label-ink: #111111;
  }
  html, body {
    margin: 0;
    padding: 0;
    width: 1200px;
    height: 1200px;
    overflow: hidden;
    background: var(--backdrop);
  }
  .canvas {
    display: block;
    width: 1200px;
    height: 1200px;
    font-family: "Inter", "Helvetica Neue", Arial, sans-serif;
  }
  .size-label { fill: var(--label-ink); font-size: 40px; font-weight: 400; letter-spacing: 1px; }
  .sign-panel { fill: var(--sign-navy); }
  .brand-ring { fill: none; stroke: var(--ring-blue); stroke-width: 4; }
  .brand-name { fill: var(--brand-mist); font-weight: 400; }
  .brand-name--main { font-size: 31px; letter-spacing: 1.5px; }
  .brand-name--sub { font-size: 16px; letter-spacing: 6px; }
  .headline { fill: var(--ink-white); font-size: 158px; font-weight: 300; letter-spacing: -2px; }
  .agent-name { fill: var(--agent-blue); font-size: 38px; font-weight: 400; }
  .agent-phone { fill: var(--ink-white); font-size: 46px; font-weight: 400; }
  .agent-web { fill: var(--ink-white); font-size: 28px; font-weight: 400; }
  .agent-licence { fill: var(--ink-white); font-size: 12px; font-weight: 400; }
</style>
</head>
<body>
<svg class="canvas" viewBox="0 0 1200 1200" xmlns="http://www.w3.org/2000/svg">
  <defs>
    <filter id="panel-shadow" x="-10%" y="-10%" width="130%" height="130%">
      <feDropShadow dx="6" dy="6" stdDeviation="4" flood-color="#000" flood-opacity="0.35"/>
    </filter>
  </defs>

  <text class="size-label" x="24" y="69">24x18</text>

  <g class="sign">
    <rect class="sign-panel" x="320" y="226" width="560" height="747" filter="url(#panel-shadow)"/>

    <g class="brand">
      <circle class="brand-ring" cx="443" cy="352" r="66"/>
      <text class="brand-name brand-name--main" x="535" y="352">GILDED HARBOR</text>
      <text class="brand-name brand-name--sub" x="537" y="382">REAL ESTATE</text>
    </g>

    <text class="headline" x="428" y="604">For</text>
    <text class="headline" x="428" y="744">Sale</text>

    <g class="agent">
      <text class="agent-name" x="433" y="826">Corinne Vasquel</text>
      <text class="agent-phone" x="431" y="879">503-841-2096</text>
      <text class="agent-web" x="432" y="918">www.gildedharbor-example.com</text>
      <text class="agent-licence" x="433" y="944">BRE Licence Number: 04817359</text>
    </g>
  </g>
</svg>
</body>
</html>
```